Heritage Hollow Business Cards

Require a business card design. <br/><br/>Needs to include logo (either round or long version) plus these details:<br/>Maya Torvel<br/>Heritage Hollow<br/>maya@quonbrook.com.au<br/>02 6481 7390<br/>PO Box Glenwarra NSW 2913<br/>www.heritagehollow.com.au<br/><br/>I need in an editable format so that I can create for multiple staff members. <br/><br/>

Target Market(s)

We are an online store selling renovation products to home owners are builders. Looking for a classic classy design.

Industry/Entity Type

Home And Garden

Contact Information for Business Card

Maya Torvel
Heritage Hollow
maya@quonbrook.com.au
02 6481 7390
PO Box Glenwarra NSW 2913
www.heritagehollow.com.au

Colors

Designer to choose colors to be used in the design.

Requirements
Must have
• Must include Logo.

```html
<!DOCTYPE html>
<html lang="en">
<head>
<meta charset="utf-8">
<title>Heritage Hollow Business Cards</title>
<link href="https://fonts.googleapis.com/css2?family=Outfit:wght@300;400;500&display=swap" rel="stylesheet">
<style>
  :root {
    --backdrop: #3b3937;
    --forest: #50715f;
    --forest-deep: #46685a;
    --paper: #ffffff;
    --ink: #2b2b2b;
    --text: #262626;
    --on-forest: #f4f4f0;
  }
  * { margin: 0; padding: 0; box-sizing: border-box; }
  html, body {
    width: 1200px; height: 900px; overflow: hidden;
    background: var(--backdrop);
    font-family: "Outfit", sans-serif;
  }
  .canvas { position: relative; width: 1200px; height: 900px; }

  .card { position: absolute; left: 311px; width: 577px; }

  /* Front */
  .card-front { top: 98px; height: 328px; background: var(--forest); }
  .front-emblem {
    position: absolute; left: 203px; top: 86px;
    width: 172px; height: 172px; border-radius: 50%;
    border: 1.5px solid var(--on-forest);
    display: flex; align-items: center; justify-content: center;
  }
  .front-emblem .brand-name {
    color: var(--on-forest); font-size: 29px; font-weight: 400;
    line-height: 30px; text-align: center;
  }
  .front-url {
    position: absolute; left: 0; right: 0; top: 290px;
    text-align: center; color: var(--on-forest); font-size: 16px; font-weight: 400;
  }

  /* Back */
  .card-back { top: 472px; height: 329px; background: var(--paper); }
  .back-brand {
    position: absolute; left: 34px; top: 46px;
    display: flex; align-items: flex-end; gap: 8px;
  }
  .brand-ring {
    width: 46px; height: 46px; border-radius: 50%;
    border: 1.5px solid var(--ink); margin-bottom: 14px;
  }
  .back-brand .brand-name { color: var(--ink); font-size: 28px; font-weight: 400; line-height: 34px; }

  .holder { position: absolute; right: 41px; top: 158px; text-align: right; }
  .holder-name { color: var(--forest-deep); font-size: 16px; font-weight: 500; line-height: 20px; }
  .holder-company { color: var(--text); font-size: 15px; font-weight: 400; line-height: 18px; }

  .divider {
    position: absolute; left: 34px; right: 41px; top: 206px;
    height: 2px; background: var(--forest-deep);
  }

  .contacts { position: absolute; left: 34px; top: 219px; list-style: none; }
  .contacts li {
    display: flex; align-items: center; gap: 8px;
    height: 26.5px; font-size: 16px; color: var(--text);
  }
  .contacts svg { width: 17px; height: 17px; fill: var(--forest-deep); flex: none; }

  .postal {
    position: absolute; right: 41px; top: 245.5px; text-align: right;
    font-size: 16px; color: var(--text); line-height: 26.5px; font-style: normal;
  }
</style>
</head>
<body>
<main class="canvas">

  <section class="card card-front">
    <div class="front-emblem">
      <span class="brand-name">Heritage<br>Hollow</span>
    </div>
    <p class="front-url">www.heritagehollow.com.au</p>
  </section>

  <section class="card card-back">
    <div class="back-brand">
      <span class="brand-ring"></span>
      <span class="brand-name">Heritage Hollow</span>
    </div>

    <div class="holder">
      <p class="holder-name">Maya Torvel</p>
      <p class="holder-company">Heritage Hollow</p>
    </div>

    <div class="divider"></div>

    <ul class="contacts">
      <li>
        <svg viewBox="0 0 24 24" aria-hidden="true"><path d="M6.6 10.8a15.1 15.1 0 0 0 6.6 6.6l2.2-2.2c.3-.3.7-.4 1-.2 1.1.4 2.3.6 3.6.6.6 0 1 .4 1 1V20c0 .6-.4 1-1 1A17 17 0 0 1 3 4c0-.6.4-1 1-1h3.5c.6 0 1 .4 1 1 0 1.3.2 2.5.6 3.6.1.3 0 .7-.2 1z"/></svg>
        <span>02 6481 7390</span>
      </li>
      <li>
        <svg viewBox="0 0 24 24" aria-hidden="true"><path d="M2 5h20v14H2zm2 2v.5l8 5 8-5V7l-8 5z"/></svg>
        <span>maya@quonbrook.com.au</span>
      </li>
      <li>
        <svg viewBox="0 0 24 24" aria-hidden="true"><path d="M12 2a10 10 0 1 0 0 20 10 10 0 0 0 0-20zm-1 17.9A8 8 0 0 1 4.2 10L9 14.8v1a2 2 0 0 0 2 2zm6.9-2.5A2 2 0 0 0 16 16h-1v-3a1 1 0 0 0-1-1H8v-2h2a1 1 0 0 0 1-1V7h2a2 2 0 0 0 2-2v-.4a8 8 0 0 1 2.9 12.8z"/></svg>
        <span>www.heritagehollow.com.au</span>
      </li>
    </ul>

    <address class="postal">
      PO Box<br>Glenwarra NSW 2913
    </address>
  </section>

</main>
</body>
</html>
```